Business Card Design

We are a new motor lodge in Hamilton NZ. Providing luxury accommodation and excellent service is the core of our business. We are looking for a different business card to capture the eye once in there hand. We have quite a lot of different clientele, corporate, travellers passing by plus we are positioned by two main hospitals so we have a lot of guests staying from there.
The existing card we have has a bed in the background with our logo. Does not stand out too much.

Delphine
Updates

To our final designers we will be making a decision today. we will be intouch

Target Market(s)

Quite a variety from single travellers to families

Industry/Entity Type

Accommodation

Contact Information for Business Card

Kirrin Motor Lodge Delphine & Marcus Oldroyd
19 Porowhita Road Hamilton 3204
Freephone 0800 615 394
Phone 07 391 4468
Fax 07 3914469
info@kirrinmotorlodge.co.nz
www.kirrinmotorlodge.co.nz

Colors

Designer to choose colors to be used in the design.

Requirements
Must have
• Name:
Address:
Phone Numbers:
Web and Email Addresses.
Kirrin Logo
map on the back of our positioning
Nice to have
• Something styley and eyecatching have included a couple of photos of the Motor Lodge

```html
<!DOCTYPE html>
<html lang="en">
<head>
<meta charset="utf-8">
<title>Kirrin Motor Lodge — Business Card</title>
<link href="https://fonts.googleapis.com/css2?family=Roboto:wght@400;500;700&display=swap" rel="stylesheet">
<style>
  :root {
    --page-bg: #e7e5e1;
    --card-black: #1a1a1b;
    --sky: #8fcaf0;
    --white: #ffffff;
    --rule: #bdbdbd;
    --emboss-grey: #5e5e60;
  }
  html, body {
    margin: 0;
    width: 1200px;
    height: 1023px;
    overflow: hidden;
    background: var(--page-bg);
    font-family: "Roboto", Arial, sans-serif;
  }
  .card {
    position: absolute;
    left: 170px;
    width: 860px;
    height: 480px;
    background: var(--card-black);
    box-shadow: 0 8px 24px rgba(0,0,0,.25);
    overflow: hidden;
  }
  .card--back { top: 24px; }
  .card--front { top: 520px; }

  /* Back side */
  .back-brand {
    position: absolute;
    inset: 0;
    display: flex;
    align-items: center;
    justify-content: center;
    gap: 28px;
  }
  .back-brand__dot {
    width: 46px;
    height: 46px;
    border-radius: 50%;
    background: var(--emboss-grey);
  }
  .back-brand__name {
    color: var(--emboss-grey);
    font-weight: 700;
    font-size: 96px;
    line-height: 1;
    letter-spacing: 4px;
    text-transform: uppercase;
  }
  .back-brand__name span { display: block; font-size: 52px; letter-spacing: 8px; margin-top: 12px; }

  /* Front side */
  .card__stripe {
    position: absolute;
    left: 0; right: 0; bottom: 0;
    height: 16px;
    background: var(--sky);
  }
  .brand {
    position: absolute;
    right: 80px;
    top: 60px;
    display: flex;
    align-items: center;
    gap: 18px;
  }
  .brand__dot {
    width: 28px;
    height: 28px;
    border-radius: 50%;
    background: var(--white);
  }
  .brand__name {
    color: var(--white);
    font-weight: 700;
    font-size: 54px;
    line-height: 1;
    letter-spacing: 2px;
    text-transform: uppercase;
  }
  .brand__name span { display: block; font-size: 32px; letter-spacing: 4px; margin-top: 8px; }
  .contact {
    position: absolute;
    left: 0; right: 0;
    top: 270px;
    display: flex;
    justify-content: center;
  }
  .contact__people {
    text-align: right;
    padding-right: 22px;
    border-right: 2px solid var(--rule);
    color: var(--white);
    font-size: 20px;
    line-height: 30px;
  }
  .contact__names { color: var(--sky); font-weight: 500; }
  .contact__lines {
    padding-left: 22px;
    color: var(--white);
    font-size: 20px;
    line-height: 30px;
  }
  .contact__line { display: flex; align-items: center; gap: 10px; }
  .contact__line svg { width: 17px; height: 17px; flex: none; }
</style>
</head>
<body>
  <div class="card card--back">
    <div class="back-brand">
      <div class="back-brand__dot"></div>
      <div class="back-brand__name">Kirrin<span>Motor Lodge</span></div>
    </div>
  </div>

  <div class="card card--front">
    <div class="brand">
      <div class="brand__dot"></div>
      <div class="brand__name">Kirrin<span>Motor Lodge</span></div>
    </div>

    <div class="contact">
      <div class="contact__people">
        <div class="contact__names">Delphine &amp; Marcus Oldroyd</div>
        <div>19 Porowhita Road</div>
        <div>Hamilton 3204</div>
        <div>www.kirrinmotorlodge.co.nz</div>
      </div>
      <div class="contact__lines">
        <div class="contact__line">
          <svg viewBox="0 0 20 20"><path d="M5 2l3 4-2 2c1 2 3 4 5 5l2-2 4 3-2 3C9 17 3 11 2 5z" fill="var(--sky)"/></svg>
          0800 615 394 (Free Phone)
        </div>
        <div class="contact__line">
          <svg viewBox="0 0 20 20"><path d="M5 2l3 4-2 2c1 2 3 4 5 5l2-2 4 3-2 3C9 17 3 11 2 5z" fill="var(--sky)"/></svg>
          07 391 4468
        </div>
        <div class="contact__line">
          <svg viewBox="0 0 20 20"><rect x="3" y="7" width="14" height="10" rx="1" fill="none" stroke="var(--sky)" stroke-width="2"/><rect x="6" y="2" width="8" height="6" fill="none" stroke="var(--sky)" stroke-width="2"/><rect x="6" y="11" width="8" height="2" fill="var(--sky)"/></svg>
          07 3914469
        </div>
        <div class="contact__line">
          <svg viewBox="0 0 20 20"><rect x="2" y="4" width="16" height="12" fill="var(--sky)"/><path d="M2 4l8 7 8-7" fill="none" stroke="var(--card-black)" stroke-width="1.6"/></svg>
          info@kirrinmotorlodge.co.nz
        </div>
      </div>
    </div>

    <div class="card__stripe"></div>
  </div>
</body>
</html>
```